Business Card Design Project

Hi,
I am after a business card design for a new business. The business is called Hollow Crest and is a stockist of building supplies used for modern cosmetic renovations for houses. (e.g Floorboards, timber decking, modern fittings and fixtures.)
The logo and font faces have been attached.
The logo comes in 2 different color scheme's - 1. Orange on White & 2. Orange on Black. I would like 2 versions of the business card design to reflect these color scheme's.
The designs need to be double sided. The front should contain all the contact information, whilst the back of the card should display the logo and the URL of the webpage - www.hollowcrest-example.com.au . The logo needs to be displayed creatively on the back of the card.
The business card design needs to reflect the image of modern living, but should also have the wow factor.

```html
<!DOCTYPE html>
<html lang="en">
<head>
<meta charset="utf-8">
<title>Hollow Crest – Business Cards</title>
<link rel="stylesheet" href="https://fonts.googleapis.com/css2?family=Michroma&family=Open+Sans:wght@400;600;700&display=swap">
<style>
  :root {
    --backdrop: #8f8f8f;
    --orange-bright: #ec6a27;
    --orange-mid: #c85418;
    --orange-deep: #9c3f0c;
    --white: #ffffff;
    --ink: #2b2b2b;
    --rule: #c9c9c9;
  }
  * { margin: 0; padding: 0; box-sizing: border-box; }
  html, body {
    width: 1200px;
    height: 900px;
    overflow: hidden;
  }
  body {
    position: relative;
    background: var(--backdrop);
    font-family: "Open Sans", Arial, sans-serif;
  }

  .card {
    position: absolute;
    left: 270px;
    width: 640px;
    height: 366px;
    overflow: hidden;
  }

  /* Front of card */
  .card-front {
    top: 50px;
    background: radial-gradient(ellipse 70% 85% at 52% 38%, var(--orange-bright) 0%, var(--orange-mid) 55%, var(--orange-deep) 100%);
  }
  .brand-panel {
    position: absolute;
    left: 34px;
    top: 30px;
    width: 196px;
    bottom: 0;
    background: var(--white);
  }
  .brand-panel .rule {
    position: absolute;
    left: 10px;
    right: 10px;
    height: 1px;
    background: var(--rule);
  }
  .brand-panel .rule-top { top: 10px; }
  .brand-panel .rule-upper-url { top: 250px; }
  .brand-panel .rule-lower-url { top: 300px; }
  .brand-mark {
    position: absolute;
    left: 0;
    right: 0;
    top: 96px;
    display: flex;
    align-items: center;
    justify-content: center;
    gap: 8px;
  }
  .brand-mark .mark-square {
    width: 22px;
    height: 22px;
    background: var(--orange-mid);
  }
  .brand-mark .brand-name {
    font-size: 23px;
    font-weight: 600;
    color: var(--ink);
    white-space: nowrap;
  }
  .panel-url {
    position: absolute;
    left: 0;
    right: 0;
    top: 262px;
    text-align: center;
    font-size: 13px;
    font-weight: 600;
    color: var(--ink);
  }

  .holder-name {
    position: absolute;
    right: 36px;
    top: 50px;
    font-family: "Michroma", "Arial Black", sans-serif;
    font-size: 30px;
    color: var(--white);
    white-space: nowrap;
  }
  .contact {
    position: absolute;
    right: 36px;
    top: 196px;
    text-align: right;
    color: var(--white);
    font-weight: 700;
    font-size: 17px;
    line-height: 30px;
  }
  .contact .email { font-size: 15px; }
  .faint-square {
    position: absolute;
    left: 550px;
    top: 298px;
    width: 40px;
    height: 40px;
    background: var(--orange-deep);
    opacity: 0.55;
  }

  /* Back of card */
  .card-back {
    top: 470px;
    height: 370px;
    background: var(--white);
  }
  .band {
    position: absolute;
    left: 0;
    right: 0;
    background: linear-gradient(90deg, var(--orange-deep), var(--orange-mid) 50%, var(--orange-deep));
  }
  .band-top { top: 0; height: 70px; }
  .band-bottom { bottom: 0; height: 84px; display: flex; align-items: center; justify-content: center; }
  .band-bottom .site-url {
    color: var(--white);
    font-size: 22px;
    font-weight: 700;
    letter-spacing: 0.3px;
  }
  .back-rule {
    position: absolute;
    left: 0;
    right: 0;
    height: 2px;
    background: var(--rule);
  }
  .back-rule-top { top: 80px; }
  .back-rule-bottom { bottom: 94px; }
  .back-logo {
    position: absolute;
    left: 0;
    right: 0;
    top: 118px;
    display: flex;
    align-items: center;
    justify-content: center;
    gap: 22px;
  }
  .back-logo .mark-square {
    width: 80px;
    height: 80px;
    background: var(--orange-mid);
  }
  .back-logo .brand-name {
    font-size: 60px;
    font-weight: 600;
    color: var(--ink);
    white-space: nowrap;
  }
</style>
</head>
<body>

  <section class="card card-front" aria-label="Card front">
    <div class="brand-panel">
      <span class="rule rule-top"></span>
      <div class="brand-mark">
        <span class="mark-square"></span>
        <span class="brand-name">Hollow Crest</span>
      </div>
      <span class="rule rule-upper-url"></span>
      <p class="panel-url">hollowcrest-example.com.au</p>
      <span class="rule rule-lower-url"></span>
    </div>

    <h1 class="holder-name">Your Name</h1>

    <div class="contact">
      <p class="address">st. Streat Address</p>
      <p class="phone">phone: +61 400 555 019</p>
      <p class="email">email: name@hollowcrest-example.com.au</p>
    </div>

    <span class="faint-square"></span>
  </section>

  <section class="card card-back" aria-label="Card back">
    <div class="band band-top"></div>
    <span class="back-rule back-rule-top"></span>
    <div class="back-logo">
      <span class="mark-square"></span>
      <span class="brand-name">Hollow Crest</span>
    </div>
    <span class="back-rule back-rule-bottom"></span>
    <div class="band band-bottom">
      <p class="site-url">www.hollowcrest-example.com.au</p>
    </div>
  </section>

</body>
</html>
```